Amber Hollow Productions

I need a business card design for a new freelance film production company using or incorporating the logo:
I want the card to be creative, minimal, yet professional. Feel free to use a variety of different shapes and sizes/ textures for the card.

Industry/Entity Type

Film Production

```html
<!DOCTYPE html>
<html lang="en">
<head>
<meta charset="utf-8">
<title>Amber Hollow Productions – Business Card</title>
<link rel="stylesheet" href="https://fonts.googleapis.com/css2?family=Source+Sans+3:wght@400&display=swap">
<style>
  :root {
    --backdrop: #1d1d1e;
    --card-light: #e6e7e8;
    --card-grey: #a7a8ab;
    --brand-blue: #1a59a8;
    --ink-dark: #38393b;
    --ink-contact: #2f3032;
  }
  * { margin: 0; padding: 0; box-sizing: border-box; }
  html, body {
    width: 1200px;
    height: 750px;
    overflow: hidden;
    background: var(--backdrop);
    font-family: "Source Sans 3", "Myriad Pro", sans-serif;
  }
  .canvas {
    position: relative;
    width: 1200px;
    height: 750px;
  }
  .card {
    position: absolute;
    left: 100px;
    top: 99px;
    width: 1000px;
    height: 552px;
    border-radius: 130px;
    overflow: hidden;
    background: var(--card-light);
  }
  .card-shape {
    position: absolute;
    inset: 0;
    width: 1000px;
    height: 552px;
  }
  .brand {
    position: absolute;
    left: 96px;
    width: 300px;
    top: 170px;
    text-align: center;
    color: var(--brand-blue);
    font-weight: 400;
  }
  .brand-square {
    display: block;
    width: 64px;
    height: 64px;
    margin: 0 auto 26px;
    background: var(--brand-blue);
  }
  .brand-name {
    font-size: 40px;
    line-height: 1.1;
    letter-spacing: 1px;
  }
  .person {
    position: absolute;
    left: 545px;
    top: 166px;
    font-size: 34px;
    line-height: 1;
    white-space: nowrap;
  }
  .person-name { color: var(--brand-blue); }
  .person-sep { color: var(--ink-dark); margin: 0 2px; }
  .person-role { color: var(--ink-dark); }
  .contact {
    position: absolute;
    left: 523px;
    width: 400px;
    top: 440px;
    text-align: center;
    font-size: 23px;
    line-height: 30px;
    color: var(--ink-contact);
    white-space: nowrap;
  }
</style>
</head>
<body>
<main class="canvas">
  <section class="card">
    <svg class="card-shape" viewBox="0 0 1000 552" aria-hidden="true">
      <path d="M595,0 C505,12 488,190 470,340 C456,462 446,515 428,552 L1000,552 L1000,0 Z" fill="var(--card-grey)"/>
    </svg>

    <div class="brand">
      <span class="brand-square"></span>
      <p class="brand-name">Amber Hollow<br>Productions</p>
    </div>

    <p class="person">
      <span class="person-name">Daniel Reyes</span><span class="person-sep"> | </span><span class="person-role">Director</span>
    </p>

    <address class="contact" style="font-style: normal;">
      412 Lantern Avenue | Chicago, IL. 606114<br>
      P: (312) 555-0194 | hello@amberhollow.com
    </address>
  </section>
</main>
</body>
</html>
```